Business Card Needed for Crafter of Pottery, Jewelry and Artwork

Calling all designers in search of an artistic challenge.

I need a new business card design for my pottery, jewelry and artwork business, Woven Glass and Tide, based in Vancouver BC.

I would like a card that is bright and inviting and preferably incorporates my logo and a sample of photos of my work while having a clean fresh look. The following contact details would preferably be included on the card as well:
• Helena Pikeworth
• Designer
• Phone: 604.555.0172
• Email: Designer@WovenGlassandTide.example
• Website: www.WovenGlassandTide.example
• Blog: www.ShapingHillside.example

The logo is attached in two color schemes in both Vector and Source formats. On past cards I’ve also included photos of my work. By including photos of the work the pieces are showcased and it catches people’s eye and prompts them to pick up the card and look at it more closely. For example, if I leave a stack in a coffee shop I want people to be drawn to the card, to pick it up and get a sense of the my product lines. Please feel free to pull photos of my work directly off of my website. If you need photos with higher pixels please let me know and I’ll email them directly to you. The website background is bffbda (191, 251, 218). I would like the business cards to match the feel of the website for consistency but the cards do not need to use the exact same colors. My website and current business card are predominantly turquoise shades. The background uses stripes provided by the website template. I don’t know the exact colors of the stripes.

My current business card is attached to show the use of photos in a design. Please note that I am not thrilled with my own design and am looking for variations and completely new designs. This example is not meant to be used as a template or starting point.

Here is some background surrounding my company:
WGT offers one of a kind jewelry, pottery, artwork and leather bags each designed with a twist. The pottery varies from rustic every day functional ware to raku artwork. The jewelry ranges from simple sterling every day pieces to multimedia pieces incorporating stone, metal, ceramics and fabric. The artwork is multimedia, typically acrylic paired with a natural element such as bark. All the bags are leather with reworked kimono fabric or patterned silk lining.

Feel free to check out my website to get a flavour for my work and the color scheme I've used on marketing materials so far. www.wovenglassandtide.example
Updates

Thank you to everyone who has submitted a design so far. I hope everyone has received some helpful feedback.

I'm going to post a survey to customers and friends asking for their votes. If you have new designs to submit please try to get them in by Saturday March 30 at noon so that I can include it in the survey launch.

Thank you

Target Market(s)

Females aged 25-65 interested in one of a kind functional pottery and jewelry.

Industry/Entity Type

Coffee Shop

Requirements
Must have
• Contact information, website, blog
Nice to have
• Logo, photos

```html
<!DOCTYPE html>
<html lang="en">
<head>
<meta charset="utf-8">
<title>Woven Glass and Tide — Business Card</title>
<link rel="stylesheet" href="https://fonts.googleapis.com/css2?family=Cinzel:wght@500&family=Tinos&display=swap">
<style>
  :root {
    --teal: #1a7d85;
    --teal-deep: #0f6970;
    --ring: #2a8f97;
    --paper: #ffffff;
    --mist: #e9eef0;
    --slate-teal: #8fadb1;
    --tile-border: #f4f6f6;
  }
  html, body {
    margin: 0;
    padding: 0;
    width: 1200px;
    height: 686px;
    overflow: hidden;
    background: var(--paper);
  }
  .card {
    position: relative;
    width: 1200px;
    height: 686px;
    overflow: hidden;
    background: var(--paper);
  }
  .masthead {
    position: absolute;
    left: 0; top: 0;
    width: 1200px;
    height: 142px;
    background: var(--paper);
  }
  .nav-item {
    position: absolute;
    top: 6px;
    margin: 0;
    font-family: "Tinos", serif;
    font-size: 32px;
    line-height: 40px;
    color: var(--teal);
    letter-spacing: 0.5px;
  }
  .nav-pottery { left: 40px; }
  .nav-jewelry { left: 292px; }
  .nav-handbags { left: 746px; }
  .nav-artwork { left: 990px; }
  .brand-mark {
    position: absolute;
    left: 523px; top: 4px;
    width: 166px; height: 166px;
    box-sizing: border-box;
    border-radius: 50%;
    border: 5px solid var(--ring);
    background: var(--paper);
    display: flex;
    align-items: center;
    justify-content: center;
    text-align: center;
    z-index: 2;
  }
  .brand-mark span {
    font-family: "Cinzel", serif;
    font-weight: 500;
    font-size: 17px;
    line-height: 1.3;
    color: var(--teal-deep);
  }
  .dashed-rule {
    position: absolute;
    left: 0; top: 142px;
  }
  .title-band {
    position: absolute;
    left: 0; top: 155px;
    width: 1200px;
    height: 268px;
    background: var(--mist);
    box-sizing: border-box;
    padding-top: 30px;
    display: flex;
    flex-direction: column;
    align-items: center;
  }
  .title {
    margin: 0;
    font-family: "Cinzel", serif;
    font-weight: 500;
    font-size: 88px;
    line-height: 112px;
    letter-spacing: 1px;
    color: var(--teal);
    text-shadow: 0 4px 5px rgba(15, 105, 112, 0.35);
    white-space: nowrap;
  }
  .contact {
    margin: 14px 0 0;
    font-family: "Tinos", serif;
    font-size: 22px;
    line-height: 32px;
    color: var(--teal-deep);
    text-align: center;
    white-space: nowrap;
  }
  .contact .sep {
    padding: 0 10px;
    color: var(--ring);
  }
  .gallery-band {
    position: absolute;
    left: 0; top: 430px;
    width: 1200px;
    height: 256px;
    background: var(--slate-teal);
  }
  .work-tile {
    position: absolute;
    top: 18px;
    width: 214px;
    height: 214px;
    box-sizing: border-box;
    border: 2px solid var(--tile-border);
  }
  .tile-pottery  { left: 18px;  background: radial-gradient(circle at 50% 45%, #8fd3d6 0%, #5aa9ae 38%, #5a4538 62%, #b9b3a8 100%); }
  .tile-earrings { left: 254px; background: linear-gradient(160deg, #f3f1ee 0%, #e6a3b0 45%, #c9e3dc 70%, #6b5445 100%); }
  .tile-handbag  { left: 494px; background: radial-gradient(ellipse at 50% 62%, #e4504c 0%, #c83c3a 38%, #eeeeec 70%, #fafafa 100%); }
  .tile-necklace { left: 731px; background: radial-gradient(circle at 50% 60%, #4d6f86 0%, #8aa0a8 35%, #cfd5d3 70%, #e8e8e6 100%); }
  .tile-raku     { left: 971px; background: radial-gradient(circle at 45% 50%, #6a8fc4 0%, #8a4f8c 40%, #c46a6a 70%, #e9e4ea 100%); }
</style>
</head>
<body>
<div class="card">
  <header class="masthead">
    <p class="nav-item nav-pottery">POTTERY</p>
    <p class="nav-item nav-jewelry">JEWELRY</p>
    <div class="brand-mark"><span>WOVEN GLASS<br>AND TIDE</span></div>
    <p class="nav-item nav-handbags">HANDBAGS</p>
    <p class="nav-item nav-artwork">ARTWORK</p>
  </header>

  <svg class="dashed-rule" width="1200" height="6" viewBox="0 0 1200 6" aria-hidden="true">
    <line x1="0" y1="3" x2="1200" y2="3" stroke="#1a7d85" stroke-width="3" stroke-dasharray="8 5"/>
  </svg>

  <section class="title-band">
    <h1 class="title">WOVEN GLASS AND TIDE</h1>
    <p class="contact">
      Helena Pikeworth, Designer<span class="sep">|</span>604.555.0172<span class="sep">|</span>Designer@WovenGlassandTide.example<br>
      www.WovenGlassandTide.example<span class="sep">|</span>Blog: www.ShapingHillside.example
    </p>
  </section>

  <section class="gallery-band">
    <div class="work-tile tile-pottery" role="img" aria-label="Photo of a small turquoise and brown glazed pottery jar"></div>
    <div class="work-tile tile-earrings" role="img" aria-label="Photo of pink and sea-green glass drop earrings hanging from driftwood"></div>
    <div class="work-tile tile-handbag" role="img" aria-label="Photo of a red leather handbag with a patterned lining"></div>
    <div class="work-tile tile-necklace" role="img" aria-label="Photo of a pendant necklace with a blue floral ceramic cabochon"></div>
    <div class="work-tile tile-raku" role="img" aria-label="Photo of an iridescent purple and blue raku fired dish"></div>
  </section>
</div>
</body>
</html>
```